Copper Lantern Podcast Business Card Design

Needing a business card with the logo design provided for Copper Lantern Podcast. I am looking for a modern style that fits the current logo.

Info:
Name: Bao Khanh
Title: Creator/Host
Email: bao@copperlanternpod.com
Phone: (405) 637-2918
www.copperlanternpod.com
Twitter: @coplanternpod
Instagram: @copperlanternpodcast
Facebook: Copper Lantern Podcast

Industry/Entity Type

Business

Font styles to use
Sans Serif

Colors
000000
ffffff

Requirements
Must have
• modern, clean design
Nice to have
• social media contact info

```html
<!DOCTYPE html>
<html lang="en">
<head>
<meta charset="utf-8">
<title>Copper Lantern Podcast – Business Card</title>
<link rel="stylesheet" href="https://fonts.googleapis.com/css2?family=Roboto+Condensed:wght@400;700&family=Roboto:wght@400&display=swap">
<style>
  :root {
    --page-bg: #d9d6d2;
    --card-bg: #eeedeb;
    --card-edge: #ffffff;
    --ink: #111111;
    --ink-soft: #2a2a2a;
    --band: #141414;
    --band-text: #ffffff;
    --band-muted: #d8d8d8;
    --shade: rgba(0, 0, 0, 0.06);
  }
  * { box-sizing: border-box; margin: 0; padding: 0; }
  html, body {
    width: 1200px;
    height: 969px;
    overflow: hidden;
    background: var(--page-bg);
  }
  .business-card {
    position: absolute;
    left: 76px;
    top: 188px;
    width: 1048px;
    height: 594px;
    border-radius: 30px;
    background: linear-gradient(160deg, var(--card-bg), #e4e2df);
    border: 2px solid var(--card-edge);
    overflow: hidden;
    font-family: "Roboto", sans-serif;
    color: var(--ink);
  }
  .background-block {
    position: absolute;
    left: 92px;
    top: 218px;
    width: 520px;
    height: 376px;
    background: var(--shade);
  }
  .name-band {
    position: absolute;
    left: 0;
    top: 54px;
    width: 711px;
    height: 108px;
    background: linear-gradient(90deg, var(--band), #2b2b2b 70%, var(--band));
    display: flex;
    align-items: center;
    padding-left: 45px;
    font-family: "Roboto Condensed", sans-serif;
    font-size: 33px;
    color: var(--band-text);
    text-transform: uppercase;
  }
  .name-band .person-name { font-weight: 700; }
  .name-band .person-role { font-weight: 400; color: var(--band-muted); margin-left: 10px; }
  .brand-square {
    position: absolute;
    left: 896px;
    top: 54px;
    width: 108px;
    height: 108px;
    background: var(--band);
  }
  .brand-name {
    position: absolute;
    right: 44px;
    top: 190px;
    text-align: right;
    font-family: "Roboto Condensed", sans-serif;
    font-weight: 700;
    font-size: 36px;
    line-height: 1;
    color: var(--ink);
  }
  .contact-list, .social-list {
    position: absolute;
    top: 446px;
    list-style: none;
    font-size: 24px;
    line-height: 33px;
    color: var(--ink-soft);
  }
  .contact-list { left: 45px; }
  .contact-list li { display: flex; align-items: center; gap: 16px; }
  .contact-list svg { width: 22px; height: 22px; fill: var(--ink-soft); flex: none; }
  .social-list { right: 40px; text-align: right; }
  .social-list li { display: flex; align-items: center; justify-content: flex-end; gap: 14px; }
  .social-list .social-dot { width: 18px; height: 18px; background: var(--ink-soft); border-radius: 3px; flex: none; }
</style>
</head>
<body>
  <div class="business-card">
    <div class="background-block" aria-hidden="true"></div>

    <div class="name-band">
      <span class="person-name">Bao Khanh</span>
      <span class="person-role">| Creator/Host</span>
    </div>

    <div class="brand-square" aria-hidden="true"></div>
    <div class="brand-name">Copper Lantern Podcast</div>

    <ul class="contact-list">
      <li>
        <svg viewBox="0 0 24 24" aria-hidden="true"><path d="M6.6 10.8a15.1 15.1 0 0 0 6.6 6.6l2.2-2.2a1 1 0 0 1 1-.25 11.4 11.4 0 0 0 3.6.57 1 1 0 0 1 1 1V20a1 1 0 0 1-1 1A17 17 0 0 1 3 4a1 1 0 0 1 1-1h3.5a1 1 0 0 1 1 1c0 1.25.2 2.45.57 3.57a1 1 0 0 1-.25 1z"/></svg>
        (405) 637-2918
      </li>
      <li>
        <svg viewBox="0 0 24 24" aria-hidden="true"><path d="M2 5h20v14H2z M4 7v1l8 5 8-5V7l-8 5z" fill-rule="evenodd"/></svg>
        bao@copperlanternpod.com
      </li>
      <li>
        <svg viewBox="0 0 24 24" aria-hidden="true"><circle cx="12" cy="12" r="10"/></svg>
        www.copperlanternpod.com
      </li>
    </ul>

    <ul class="social-list">
      <li>Copper Lantern Podcast <span class="social-dot" aria-hidden="true"></span></li>
      <li>@copperlanternpodcast <span class="social-dot" aria-hidden="true"></span></li>
      <li>@coplanternpod <span class="social-dot" aria-hidden="true"></span></li>
    </ul>
  </div>
</body>
</html>
```